Vasko Lumen Entertainment

I need a web design for my Business for better online promotions and services.. The name of my company is Vasko Lumen its a entertainment company music, events, networking and so on.. What I do is help artist create and finish projects such as mix tapes, music videos, and book performances in order to create a platform and i also offer representation to help grow there brands or business... I also work with and help develop independent artists!!!

Target Market(s)

Hip hop and R&B industry

Industry/Entity Type

Entertainment Industry

Number of Pages Required

1 page

Requirements
Must have
• Must display My previous and upcoming work i want people to see the quality I provide in my service.. I have more videos that I want to upload on there to show more work.... I would like to bring all the separate promotions and campaigns that I previously had and currently have all one platform for everybody to see and to find more easily instead having everything so spread out..
Nice to have
• Creativity thats going to compliment my work and quality..

```html
<!DOCTYPE html>
<html lang="en">
<head>
<meta charset="utf-8">
<title>Vasko Lumen</title>
<link href="https://fonts.googleapis.com/css2?family=Lato:wght@300;400;700&family=Varela+Round&family=Roboto+Slab:wght@700&family=Source+Sans+3:wght@400;600&display=swap" rel="stylesheet">
<style>
:root{
  --red:#ed2129;
  --black:#000;
  --panel:rgba(40,40,40,.78);
  --white:#fff;
  --grey-text:#8a8a8a;
  --card:#fff;
  --stone:#4a4a4a;
}
*{margin:0;padding:0;box-sizing:border-box}
html,body{width:1200px;height:2821px;overflow:hidden;background:var(--black)}
body{position:relative;font-family:"Varela Round",sans-serif;color:var(--white)}
.abs{position:absolute}
.backdrop{left:0;top:0;width:1200px;height:1340px;background:radial-gradient(ellipse at 10% 40%,#1d3a1e 0%,transparent 40%),radial-gradient(ellipse at 95% 50%,#1f3b1c 0%,transparent 35%),linear-gradient(#1b1b1b,#0c0c0c 70%,#000)}
.site-header{left:0;top:0;width:1200px;height:113px;background:linear-gradient(90deg,#5a5a5a,#7a7a7a 40%,#5d5d5d 70%,#6e6e6e)}
.logo-box{left:113px;top:0;width:197px;height:113px;background:#111;display:flex;align-items:center;justify-content:center;gap:8px}
.logo-mark{width:14px;height:14px;background:var(--red)}
.logo-name{font-family:"Varela Round",sans-serif;font-size:22px;color:var(--red)}
.main-nav{left:456px;top:50px;display:flex;gap:0}
.main-nav a{font-family:"Roboto Slab",serif;font-size:17px;color:var(--white);text-decoration:none;margin-right:55px;text-shadow:0 1px 2px #000}
.hero{left:113px;top:117px;width:969px;height:413px;background:linear-gradient(180deg,#8c8c8c,#5f5f5f 50%,#2c2c2c)}
.hero-title{left:113px;top:316px;width:969px;text-align:center;font-family:"Lato",sans-serif;font-weight:300;font-size:43px;letter-spacing:11px;line-height:50px}
.welcome{left:113px;top:559px;width:969px;height:220px;background:var(--panel);text-align:center;padding-top:28px}
.welcome h2{font-family:"Lato",sans-serif;font-weight:300;font-size:40px;letter-spacing:1px;margin-bottom:8px}
.welcome p{font-size:15px;line-height:23px;width:900px;margin:0 auto}
.section-title{width:1200px;left:0;text-align:center;font-family:"Lato",sans-serif;font-weight:300;font-size:40px}
.work-tile{height:244px}
.work-tile .thumb{width:100%;height:210px}
.work-bar{height:34px;background:var(--red);display:flex;align-items:center;justify-content:space-between;padding:0 18px}
.work-bar span{font-family:"Roboto Slab",serif;font-size:16px}
.more-link{right:117px;top:1480px;display:flex;align-items:center;gap:10px;font-family:"Roboto Slab",serif;font-size:16px;color:var(--red);letter-spacing:1px}
.team{left:118px;top:1561px;width:969px;height:580px;background:linear-gradient(135deg,#8a8a8a,#5a5a5a 45%,#3b3b3b 80%,#2a2a2a)}
.team-title{top:1593px}
.team-rule{left:558px;top:1662px;width:96px;height:2px;background:rgba(255,255,255,.4)}
.member{top:1702px;width:218px;height:412px;background:var(--card)}
.member .photo{height:222px}
.member-info{padding:22px 20px 0;font-family:"Source Sans 3",sans-serif}
.member-info h3{font-weight:400;font-size:16px;color:#555;letter-spacing:.5px}
.member-info h4{font-weight:400;font-size:10px;color:#999;margin:3px 0 14px}
.member-info p{font-size:14px;line-height:24px;color:var(--grey-text)}
.event-title{left:173px;top:2290px;font-family:"Lato",sans-serif;font-weight:300;font-size:34px;letter-spacing:1px}
.event-text{left:173px;top:2352px;width:500px;font-size:15px;line-height:24.5px}
.event-photo{left:726px;top:2250px;width:327px;height:259px;background:linear-gradient(160deg,#d8d6cc,#8d8a80 55%,#2f2d29)}
.event-bar{left:726px;top:2509px;width:327px;height:30px;background:var(--red);display:flex;align-items:center;justify-content:space-between;padding:0 20px}
.event-bar span{font-family:"Roboto Slab",serif;font-size:16px}
.footer{left:0;top:2605px;width:1200px;height:170px;background:linear-gradient(#1e1e1e,#141414)}
.footer-logo{left:171px;top:2633px;width:186px;height:123px;background:linear-gradient(#3a3a3a,#151515);display:flex;align-items:center;justify-content:center;gap:8px}
.footer h3{font-family:"Lato",sans-serif;font-weight:700;font-size:33px}
.footer-links{left:396px;top:2688px;display:grid;grid-template-columns:84px auto;font-family:"Roboto Slab",serif;font-size:13px;letter-spacing:2px;line-height:20px}
.subscribe{left:666px;top:2709px;display:flex}
.subscribe .email{width:274px;height:47px;background:var(--red);font-family:"Roboto Slab",serif;font-size:15px;padding:15px 20px}
.subscribe .btn{width:140px;height:47px;background:var(--white);color:#000;font-family:"Source Sans 3",sans-serif;font-size:20px;display:flex;align-items:center;justify-content:center}
.copyright{left:0;top:2775px;width:1200px;height:46px;background:var(--red);text-align:center;font-family:"Roboto Slab",serif;font-size:15px;letter-spacing:1px;line-height:46px}
</style>
</head>
<body>
<div class="abs backdrop"></div>

<header class="abs site-header" role="img" aria-label="Stone wall texture"></header>
<div class="abs logo-box"><span class="logo-mark"></span><span class="logo-name">Vasko Lumen</span></div>
<nav class="abs main-nav"><a>HOME</a><a>ABOUT</a><a>GALLERY</a><a>MUSIC</a><a>CONTACT</a></nav>

<div class="abs hero" role="img" aria-label="Black and white photo of the artist standing beside a parked van"></div>
<h1 class="abs hero-title">RIO VANCE<br>THE MONARCH</h1>

<section class="abs welcome">
  <h2>WELCOME</h2>
  <p>Lorem ipsum dolor sit amet, consectetur adipisicing elit, sed do eiusmod tempor incididunt ut labore et dolore magna aliqua. Ut enim ad minim veniam, quis nostru. Lorem ipsum dolor sit amet, consectetur adipisicing elit, sed do eiusmod tempor incididunt ut labore et dolore magna aliqua.</p>
</section>

<h2 class="abs section-title" style="top:815px">OUR WORK</h2>

<div class="abs work-tile" style="left:118px;top:903px;width:311px"><div class="thumb" role="img" aria-label="Album cover with a club stage in blue light" style="background:linear-gradient(135deg,#2233cc,#5a8cff 50%,#1a1a66)"></div><div class="work-bar"><span>MY ALBUM</span><svg width="22" height="22"><circle cx="11" cy="11" r="9" fill="none" stroke="#fff" stroke-width="2"/><path d="M9 7l5 4-5 4z" fill="#fff"/></svg></div></div>
<div class="abs work-tile" style="left:459px;top:903px;width:303px"><div class="thumb" role="img" aria-label="Album cover with the artist under pink light" style="background:linear-gradient(135deg,#d2264f,#ff6a5a 50%,#3a0f1c)"></div><div class="work-bar"><span>MY ALBUM</span><svg width="22" height="22"><circle cx="11" cy="11" r="9" fill="none" stroke="#fff" stroke-width="2"/><path d="M9 7l5 4-5 4z" fill="#fff"/></svg></div></div>
<div class="abs work-tile" style="left:792px;top:903px;width:291px"><div class="thumb" role="img" aria-label="Album cover with the artist on a dark stage" style="background:linear-gradient(135deg,#3a1a12,#8a3a2a 50%,#140a08)"></div><div class="work-bar"><span>MY ALBUM</span><svg width="22" height="22"><circle cx="11" cy="11" r="9" fill="none" stroke="#fff" stroke-width="2"/><path d="M9 7l5 4-5 4z" fill="#fff"/></svg></div></div>
<div class="abs work-tile" style="left:118px;top:1189px;width:311px"><div class="thumb" role="img" aria-label="Black and white group shot and artist title card" style="background:linear-gradient(#eaeaea,#6e6e6e 50%,#9a9a9a)"></div><div class="work-bar"><span>MY ALBUM</span><svg width="22" height="22"><circle cx="11" cy="11" r="9" fill="none" stroke="#fff" stroke-width="2"/><path d="M9 7l5 4-5 4z" fill="#fff"/></svg></div></div>
<div class="abs work-tile" style="left:459px;top:1189px;width:303px"><div class="thumb" role="img" aria-label="Event flyer with artists and a luxury car" style="background:linear-gradient(#1d1d24,#2a2a33 50%,#5a1a1f)"></div><div class="work-bar"><span>MY ALBUM</span><svg width="22" height="22"><circle cx="11" cy="11" r="9" fill="none" stroke="#fff" stroke-width="2"/><path d="M9 7l5 4-5 4z" fill="#fff"/></svg></div></div>
<div class="abs work-tile" style="left:792px;top:1189px;width:291px"><div class="thumb" role="img" aria-label="Black and white group shot and artist title card" style="background:linear-gradient(#eaeaea,#6e6e6e 50%,#9a9a9a)"></div><div class="work-bar"><span>MY ALBUM</span><svg width="22" height="22"><circle cx="11" cy="11" r="9" fill="none" stroke="#fff" stroke-width="2"/><path d="M9 7l5 4-5 4z" fill="#fff"/></svg></div></div>

<div class="abs more-link"><span>CLICK HERE FOR MORE SONGS</span><svg width="30" height="30"><circle cx="15" cy="15" r="13" fill="none" stroke="#ed2129" stroke-width="2.5"/><path d="M15 8v14M8 15h14" stroke="#ed2129" stroke-width="2.5"/></svg></div>

<section class="abs team" role="img" aria-label="Smoky grey backdrop"></section>
<h2 class="abs section-title team-title" style="font-size:34px">MEET OUR TEAM</h2>
<div class="abs team-rule"></div>

<article class="abs member" style="left:139px"><div class="photo" role="img" aria-label="Portrait of a team member in a white shirt" style="background:linear-gradient(#e2e6c8,#9aa080)"></div><div class="member-info"><h3>DANA WHITLOW</h3><h4>CEO</h4><p>Lorem ipsum dolor sit amet, consetetur sadipscing elitr, sed diam nonumy eirmod.</p></div></article>
<article class="abs member" style="left:377px"><div class="photo" role="img" aria-label="Portrait of a team member in a black hat" style="background:linear-gradient(#c8ccd6,#2a2a2a)"></div><div class="member-info"><h3>DANA WHITLOW</h3><h4>CHIEF OFFICER</h4><p>Lorem ipsum dolor sit amet, consetetur sadipscing elitr, sed diam nonumy eirmod.</p></div></article>
<article class="abs member" style="left:615px"><div class="photo" role="img" aria-label="Portrait of a team member in sunglasses" style="background:linear-gradient(#d6d9dc,#4a5a6a)"></div><div class="member-info"><h3>COREY MADDOX</h3><h4>CREATIVE DIRECTOR</h4><p>Lorem ipsum dolor sit amet, consetetur sadipscing elitr, sed diam nonumy eirmod.</p></div></article>
<article class="abs member" style="left:852px"><div class="photo" role="img" aria-label="Portrait of a team member in a white shirt" style="background:linear-gradient(#e6d8ea,#a09aa8)"></div><div class="member-info"><h3>TESSA LORNE</h3><h4>CREATIVE DIRECTOR</h4><p>Lorem ipsum dolor sit amet, consetetur sadipscing elitr, sed diam nonumy eirmod.</p></div></article>

<h2 class="abs event-title">UPCOMING EVENT</h2>
<p class="abs event-text">Lorem ipsum dolor sit amet, consectetur adipisicing elit, sed do eiusmod tempor incididunt ut labore et dolore magna aliqua. Ut enim ad minim veniam, quis nostru.<br>Lorem ipsum dolor sit amet, consectetur adipisicing elit, sed do eiusmod tempor incididunt ut labore et dolore magna aliqua. Ut enim ad minim veniam, quis nostru.</p>
<div class="abs event-photo" role="img" aria-label="Three artists posing together"></div>
<div class="abs event-bar"><span>Events</span><svg width="36" height="16"><path d="M10 2L4 8l6 6M26 2l6 6-6 6" fill="none" stroke="#fff" stroke-width="3"/></svg></div>

<svg class="abs" style="left:0;top:2596px" width="1200" height="10"><defs><pattern id="zig" width="14" height="10" patternUnits="userSpaceOnUse"><path d="M0 10L7 0l7 10z" fill="#1e1e1e"/></pattern></defs><rect width="1200" height="10" fill="url(#zig)"/></svg>
<footer class="abs footer" role="img" aria-label="Dark crowd backdrop"></footer>
<div class="abs footer-logo"><span class="logo-mark"></span><span class="logo-name">Vasko Lumen</span></div>
<h3 class="abs" style="left:395px;top:2640px;font-family:Lato,sans-serif;font-weight:700;font-size:33px">NAVIGATION</h3>
<div class="abs footer-links"><span>HOME</span><span>NEWS</span><span>MUSIC</span><span></span><span>ARTISTE</span><span></span></div>
<h3 class="abs" style="left:662px;top:2640px;font-family:Lato,sans-serif;font-weight:700;font-size:33px">CONNECT WITH MUSIC</h3>
<div class="abs subscribe"><div class="email">Type your email</div><div class="btn">Subscribe</div></div>
<div class="abs copyright">Copyright 2017 Vasko Lumen.</div>
</body>
</html>
```